Brightfield Sunray Panel cleaning business needs a flyer designed.

I need a flyer design for a new company based in Los Angeles. We clean solar panels at an affordable price, we're insured, and licensed. we would like the design to include the colors Red, white, and Blue. The flyer should emphasize the importance of cleaning solar panels to maintain the warranty and add longevity to the solar panels.

```html
<!DOCTYPE html>
<html lang="en">
<head>
<meta charset="utf-8">
<title>Brightfield Sunray Panel Cleaning Flyer</title>
<link href="https://fonts.googleapis.com/css2?family=Anton&family=Montserrat:ital,wght@0,500;0,600;0,700;0,800;1,500;1,700;1,800&display=swap" rel="stylesheet">
<style>
  :root {
    --red: #e51c24;
    --deep-red: #c21d26;
    --orange: #e8822a;
    --blue: #1f4fa8;
    --navy: #223a8f;
    --royal: #1a55b0;
    --white: #ffffff;
    --ink-blue: #2046a3;
    --grey-text: #4a4a4a;
    --rule: #9a9a9a;
  }
  * { margin: 0; padding: 0; box-sizing: border-box; }
  html, body { width: 916px; height: 1200px; overflow: hidden; background: var(--white); }
  .flyer {
    position: relative; width: 916px; height: 1200px; overflow: hidden;
    background: var(--white); font-family: "Montserrat", sans-serif;
  }
  .hero-art { position: absolute; left: 0; top: 0; width: 916px; height: 700px; }
  .brand-name {
    position: absolute; top: 44px; left: 0; width: 100%; text-align: center;
    font-family: "Montserrat", sans-serif; font-weight: 800; font-size: 56px;
    color: var(--white); letter-spacing: 1px; line-height: 1;
  }
  .brand-dot {
    display: inline-block; width: 14px; height: 14px; border-radius: 50%;
    background: var(--white); margin-left: 10px; vertical-align: middle;
  }
  .trust-seal {
    position: absolute; left: 70px; top: 164px; width: 160px; height: 160px;
  }
  .headline {
    position: absolute; left: 52px; font-family: "Anton", sans-serif;
    transform: skewX(-10deg); line-height: 1; text-transform: uppercase;
  }
  .headline--solar {
    top: 380px; font-size: 92px; letter-spacing: 1px;
    background: linear-gradient(180deg, #ffffff 10%, #c9d9ec 50%, #5db7e8 100%);
    -webkit-background-clip: text; background-clip: text; color: transparent;
  }
  .headline--cleaning { top: 478px; font-size: 90px; color: var(--white); }
  .service-area {
    position: absolute; left: 50px; top: 576px; font-weight: 700; font-style: italic;
    font-size: 27px; color: var(--white);
  }
  .feature-photo { position: absolute; top: 632px; width: 312px; height: 148px; }
  .feature-photo--one { left: 30px; }
  .feature-photo--two { left: 298px; }
  .feature-photo--three { left: 568px; }
  .feature-caption {
    position: absolute; top: 801px; font-weight: 800; font-style: italic;
    font-size: 20px; line-height: 22px; color: var(--ink-blue);
  }
  .feature-caption--one { left: 37px; }
  .feature-caption--two { left: 305px; }
  .feature-caption--three { left: 572px; }
  .divider { position: absolute; left: 33px; top: 874px; width: 852px; height: 1px; background: var(--rule); }
  .section-banner { position: absolute; left: 210px; top: 886px; width: 480px; height: 46px; }
  .section-banner__text {
    position: absolute; left: 0; top: 0; width: 100%; height: 100%;
    display: flex; align-items: center; justify-content: center;
    color: var(--white); font-weight: 600; font-size: 24px;
  }
  .benefit { position: absolute; top: 960px; width: 290px; }
  .benefit--energy { left: 30px; }
  .benefit--investment { left: 300px; }
  .benefit--longevity { left: 605px; }
  .benefit__head { display: flex; align-items: flex-start; gap: 14px; height: 70px; }
  .benefit__icon { flex: none; width: 82px; height: 66px; }
  .benefit__title {
    font-weight: 700; font-size: 21px; line-height: 24px; color: var(--ink-blue);
    text-transform: uppercase;
  }
  .benefit__rule { height: 1px; background: var(--rule); margin-top: 4px; width: 250px; }
  .benefit__text {
    margin-top: 12px; font-style: italic; font-weight: 500; font-size: 17px;
    line-height: 24px; color: var(--grey-text);
  }
  .footer-art { position: absolute; left: 0; top: 1098px; width: 916px; height: 102px; }
  .call-line {
    position: absolute; left: 37px; top: 1119px; font-weight: 700; font-size: 26px;
    color: var(--ink-blue);
  }
  .call-line__accent { color: var(--red); }
  .phone {
    position: absolute; left: 472px; top: 1104px; width: 420px;
    display: flex; align-items: center; gap: 14px; color: var(--white);
  }
  .phone__icon { width: 30px; height: 30px; }
  .phone__number { font-weight: 700; font-size: 50px; letter-spacing: 2px; line-height: 1; }
  .phone__cta {
    position: absolute; left: 470px; top: 1163px; font-weight: 600; font-size: 15px;
    letter-spacing: 2.4px; color: var(--white); text-transform: uppercase;
  }
</style>
</head>
<body>
<main class="flyer">
  <svg class="hero-art" viewBox="0 0 916 700" aria-hidden="false">
    <defs>
      <linearGradient id="heroWash" x1="0" y1="0" x2="0.4" y2="1">
        <stop offset="0" stop-color="#c9202a"/>
        <stop offset="0.28" stop-color="#d9542a"/>
        <stop offset="0.45" stop-color="#8a6a5a"/>
        <stop offset="0.7" stop-color="#2f4f9e"/>
        <stop offset="1" stop-color="#22419c"/>
      </linearGradient>
      <linearGradient id="sunGlow" x1="0" y1="0" x2="1" y2="0.4">
        <stop offset="0" stop-color="#c21d26" stop-opacity="0"/>
        <stop offset="0.6" stop-color="#e8822a" stop-opacity="0.75"/>
        <stop offset="1" stop-color="#f3b13a" stop-opacity="0.85"/>
      </linearGradient>
      <linearGradient id="slashFade" x1="0" y1="1" x2="0.3" y2="0">
        <stop offset="0" stop-color="#e51c24"/>
        <stop offset="0.6" stop-color="#ef5a62"/>
        <stop offset="1" stop-color="#ffffff" stop-opacity="0.2"/>
      </linearGradient>
      <linearGradient id="photoBlue" x1="0" y1="0" x2="1" y2="1">
        <stop offset="0" stop-color="#c5d8ee"/><stop offset="1" stop-color="#2f5fb8"/>
      </linearGradient>
      <linearGradient id="photoGreen" x1="0" y1="0" x2="1" y2="1">
        <stop offset="0" stop-color="#2f8f3a"/><stop offset="0.6" stop-color="#e9ece9"/><stop offset="1" stop-color="#3a3a3a"/>
      </linearGradient>
      <linearGradient id="photoGrey" x1="0" y1="0" x2="1" y2="1">
        <stop offset="0" stop-color="#9fb0c4"/><stop offset="0.6" stop-color="#c0876a"/><stop offset="1" stop-color="#5a6a86"/>
      </linearGradient>
    </defs>
    <rect width="916" height="700" fill="#ffffff"/>
    <g role="img" aria-label="Photo of a worker rinsing rooftop solar panels with a water hose at sunset">
      <rect width="916" height="700" fill="url(#heroWash)"/>
      <rect width="916" height="420" fill="url(#sunGlow)"/>
    </g>
    <rect width="916" height="70" fill="#c21d26" opacity="0.85"/>
    <polygon points="916,320 916,700 600,700 760,630" fill="#ffffff"/>
    <polygon points="916,180 916,300 720,660 640,660" fill="url(#slashFade)"/>
    <polygon points="916,380 916,700 780,700" fill="#ffffff"/>
    <polygon points="0,700 0,655 150,655 150,700" fill="#22419c"/>
    <polygon points="0,632 0,700 30,700 60,632" fill="#22419c"/>
    <rect x="0" y="632" width="916" height="68" fill="#ffffff" opacity="0"/>
  </svg>

  <div class="brand-name">Brightfield Sunray<span class="brand-dot"></span></div>

  <svg class="trust-seal" viewBox="0 0 160 160" aria-hidden="true">
    <circle cx="80" cy="80" r="78" fill="#e51c24"/>
    <circle cx="80" cy="80" r="62" fill="#ffffff"/>
    <circle cx="80" cy="80" r="48" fill="none" stroke="#223a8f" stroke-width="3"/>
  </svg>

  <div class="headline headline--solar">Solar Panel</div>
  <div class="headline headline--cleaning">Cleaning</div>
  <div class="service-area">Serving Los Angeles</div>

  <svg class="feature-photo feature-photo--one" viewBox="0 0 312 148" role="img" aria-label="Photo of a worker wiping solar panels with a long squeegee">
    <polygon points="62,0 312,0 250,148 0,148" fill="url(#photoBlue)"/>
  </svg>
  <svg class="feature-photo feature-photo--two" viewBox="0 0 312 148" role="img" aria-label="Photo of hands with a notebook beside a small solar panel model">
    <polygon points="62,0 312,0 250,148 0,148" fill="url(#photoGreen)"/>
  </svg>
  <svg class="feature-photo feature-photo--three" viewBox="0 0 312 148" role="img" aria-label="Photo of a technician in a hard hat inspecting solar panels">
    <polygon points="62,0 312,0 250,148 0,148" fill="url(#photoGrey)"/>
  </svg>

  <p class="feature-caption feature-caption--one">Affordable &amp;<br>Reliable Service</p>
  <p class="feature-caption feature-caption--two">Licensed &amp; Insured<br>for Your Peace<br>of Mind</p>
  <p class="feature-caption feature-caption--three">Extend Your Solar<br>Panel’s Lifespan &amp;<br>Warranty</p>

  <div class="divider"></div>

  <div class="section-banner">
    <svg width="480" height="46" viewBox="0 0 480 46" aria-hidden="true">
      <polygon points="22,0 480,0 458,46 0,46" fill="#e51c24"/>
    </svg>
    <div class="section-banner__text">Why Clean Your Solar Panels?</div>
  </div>

  <section class="benefit benefit--energy">
    <div class="benefit__head">
      <svg class="benefit__icon" viewBox="0 0 82 66" fill="none" stroke="#e51c24" stroke-width="2.4" aria-hidden="true">
        <line x1="22" y1="20" x2="22" y2="60"/><circle cx="22" cy="18" r="3"/>
        <path d="M22 18 L14 4 M22 18 L36 20 M22 18 L12 28"/>
        <circle cx="60" cy="18" r="6"/>
        <path d="M60 6v-4 M60 30v4 M48 18h-4 M72 18h4 M52 10l-3-3 M68 10l3-3 M52 26l-3 3 M68 26l3 3"/>
        <polygon points="38,44 74,44 78,60 34,60"/>
        <path d="M48 44 L46 60 M60 44 L62 60 M36 52 H76"/>
        <line x1="4" y1="62" x2="80" y2="62"/>
      </svg>
      <h3 class="benefit__title">Boost<br>Energy<br>Efficiency</h3>
    </div>
    <div class="benefit__rule" style="width:290px"></div>
    <p class="benefit__text">Dirt &amp; debris reduce<br>solar output</p>
  </section>

  <section class="benefit benefit--investment">
    <div class="benefit__head">
      <svg class="benefit__icon" viewBox="0 0 82 66" fill="none" stroke="#e51c24" stroke-width="2.6" aria-hidden="true">
        <path d="M22 4 L42 10 L62 4 V30 C62 48 50 58 42 63 C34 58 22 48 22 30 Z"/>
        <circle cx="42" cy="24" r="5"/>
        <rect x="30" y="32" width="24" height="14"/>
        <path d="M42 32 V46 M30 39 H54 M42 46 V52 M36 52 H48"/>
      </svg>
      <h3 class="benefit__title">Protect<br>Your<br>Investment</h3>
    </div>
    <div class="benefit__rule" style="width:300px"></div>
    <p class="benefit__text">Regular cleaning maintains<br>your panel’s warranty</p>
  </section>

  <section class="benefit benefit--longevity">
    <div class="benefit__head">
      <svg class="benefit__icon" viewBox="0 0 82 66" fill="none" stroke="#e51c24" stroke-width="2.4" aria-hidden="true">
        <circle cx="40" cy="14" r="6"/>
        <path d="M40 2v-2 M40 26v3 M28 14h-4 M52 14h4"/>
        <path d="M6 18 a5 5 0 0 1 10 0 h-10 M66 14 a5 5 0 0 1 10 0 h-10"/>
        <rect x="6" y="38" width="16" height="24" rx="2"/><rect x="11" y="34" width="6" height="4"/>
        <path d="M15 44 L11 51 H16 L12 58"/>
        <polygon points="34,40 70,40 64,62 28,62"/>
        <path d="M46 40 L40 62 M58 40 L52 62 M31 51 H67"/>
        <path d="M40 26 L52 38"/>
      </svg>
      <h3 class="benefit__title">Increase<br>Longevity</h3>
    </div>
    <div class="benefit__rule" style="width:290px"></div>
    <p class="benefit__text">Well-maintained panels<br>last longer &amp; perform better</p>
  </section>

  <svg class="footer-art" viewBox="0 0 916 102" aria-hidden="true">
    <polygon points="0,74 420,74 408,102 0,102" fill="#e51c24"/>
    <polygon points="448,0 916,0 916,102 400,102" fill="#1a55b0"/>
  </svg>

  <p class="call-line">Call Now for a <span class="call-line__accent">Free Quote!</span></p>

  <div class="phone">
    <svg class="phone__icon" viewBox="0 0 30 30" aria-hidden="true">
      <path d="M7 3 L11 3 L13 10 L10 12 C11.5 16 14 18.5 18 20 L20 17 L27 19 L27 23 C27 25 25 27 23 27 C13 26 4 17 3 7 C3 5 5 3 7 3 Z" fill="#e51c24"/>
      <path d="M18 4 A9 9 0 0 1 26 12 M18 8 A5 5 0 0 1 22 12" fill="none" stroke="#e51c24" stroke-width="2"/>
    </svg>
    <span class="phone__number">800-555-0142</span>
  </div>
  <p class="phone__cta">Schedule your cleaning today</p>
</main>
</body>
</html>
```